New Template design for Website in Wordpress

We are interested in changing our website look at www.cargolinx.com -We also are very interested in Have it done in Wordpress in which we are understanding the search engines are liking a bit more. The website we would want to try working with on this is www.cargolinx.com. We look forward to seeing the different design ideas please just make sure they are in wordpress! Thanks, Marlen

Reason: need more design idea..... We would still like to use our pictures off our site since we paid for them so keep that in mind as well as we would still want the rotating pictures in the head of the page but not in Flash.

```html
<!DOCTYPE html>
<html lang="en">
<head>
<meta charset="utf-8">
<title>Cargo Linx – Worldwide Shipping</title>
<link href="https://fonts.googleapis.com/css2?family=Open+Sans:ital,wght@0,400;0,600;0,700;1,400&family=Oswald:wght@400;500&display=swap" rel="stylesheet">
<style>
:root{
  --blue:#1f6fae;
  --blue-dark:#16507f;
  --navy:#1d3347;
  --bar:#2b3e50;
  --orange:#e8771f;
  --ink:#333;
  --muted:#666;
  --line:#d9dde1;
  --page:#eef0f2;
  --white:#fff;
  --footer:#1a4a73;
}
*{box-sizing:border-box;margin:0;padding:0}
html,body{width:1200px;height:2596px;overflow:hidden}
body{font-family:"Open Sans",Arial,sans-serif;color:var(--ink);background:var(--white);font-size:15px;line-height:1.55}
.wrap{width:1096px;margin:0 auto;position:relative}

/* header */
.site-header{height:120px;border-bottom:1px solid var(--line)}
.social{position:absolute;left:0;top:8px;display:flex;gap:6px}
.social span{width:22px;height:22px;background:var(--blue);display:block;border-radius:2px}
.topline{position:absolute;left:118px;top:9px;font-size:13px;color:var(--muted)}
.topline b{color:var(--blue)}
.brand{position:absolute;left:0;top:50px;display:flex;align-items:center;gap:10px}
.brand .mark{width:26px;height:26px;background:var(--navy);display:block}
.brand .name{font-weight:700;font-size:28px;color:var(--navy);line-height:1}
.main-nav{position:absolute;right:0;top:70px;display:flex;font-size:14px;font-weight:600}
.main-nav a{padding:12px 20px;color:var(--navy);text-decoration:none;border-bottom:3px solid transparent}
.main-nav a.active{color:var(--blue);border-bottom-color:var(--blue)}

/* hero */
.hero{height:440px;position:relative;background:linear-gradient(180deg,#7fa9d0 0%,#b9cde0 45%,#8a8f86 62%,#5d5f58 100%)}
.hero-caption{position:absolute;left:0;right:0;bottom:0;height:90px;background:rgba(15,30,45,.55);display:flex;align-items:center;justify-content:center}
.hero-caption h1{font-family:"Oswald",sans-serif;font-weight:500;font-size:40px;color:var(--white);letter-spacing:1px}

/* services */
.services{height:500px;padding-top:40px}
.services-lead{text-align:center;font-weight:700;font-size:19px;color:var(--navy)}
.services-lead a{color:var(--blue);text-decoration:none}
.service-grid{display:grid;grid-template-columns:repeat(4,1fr);gap:32px;margin-top:60px;text-align:center}
.service-icon{width:100px;height:100px;border-radius:50%;background:var(--navy);margin:0 auto;display:flex;align-items:center;justify-content:center}
.service-icon.active{background:#2d6da3;box-shadow:0 0 0 5px #cfe0ef}
.service h3{font-family:"Oswald",sans-serif;font-weight:500;font-size:26px;color:var(--navy);margin-top:22px;white-space:nowrap}
.service.active h3{color:var(--orange)}
.service p{font-size:13px;color:var(--muted);margin:8px auto 0;width:220px;line-height:1.5}
.btn-more{display:inline-block;margin-top:16px;background:var(--navy);color:var(--white);font-size:12px;padding:5px 26px;text-decoration:none}

/* content */
.content-band{background:var(--page);height:1284px;padding-top:36px;border-top:1px solid var(--line)}
.content-grid{display:grid;grid-template-columns:880px 184px;gap:32px;align-items:stretch}
.main-col{background:var(--white);padding:24px 28px 30px}
.main-col h2{font-family:"Oswald",sans-serif;font-weight:500;font-size:24px;color:var(--blue)}
.bar-title{background:var(--bar);color:var(--white);font-weight:700;font-size:14px;padding:10px 16px;margin-top:14px;letter-spacing:.3px}
.main-col .text{font-size:14.5px;color:var(--muted);margin-top:16px;line-height:1.75}
.main-col .callout{font-family:"Oswald",sans-serif;font-size:25px;color:var(--blue);line-height:1.3;margin:24px 0 26px}
.video{height:470px;position:relative;background:linear-gradient(180deg,#6f8fb0 0%,#9fb6c8 40%,#3c5a78 100%)}
.play{position:absolute;left:50%;top:50%;width:84px;height:58px;margin:-29px 0 0 -42px;background:#d22;border-radius:12px;display:flex;align-items:center;justify-content:center}
.testimonial{display:flex;gap:34px;margin-top:44px;align-items:center}
.avatar{width:180px;height:180px;border-radius:50%;background:linear-gradient(180deg,#d9dde2,#b8c0c8);border:5px solid #e6e9ec;flex:none}
.quote{flex:1;position:relative;padding-left:34px}
.quote .mark{position:absolute;left:0;top:-4px;font-family:"Oswald",sans-serif;font-size:56px;color:#c9ced3;line-height:1}
.quote p{font-size:14.5px;color:var(--muted);font-style:italic;line-height:1.75}
.quote cite{display:block;font-size:14px;color:var(--blue);margin-top:12px;font-style:normal}

/* sidebar */
.side-col{font-size:12px}
.quote-btn{display:block;background:var(--blue);color:var(--white);font-weight:700;padding:10px 12px;text-decoration:none;font-size:13px;line-height:1.2}
.quote-btn small{display:block;font-weight:400;font-size:10px;margin-top:2px}
.side-phone{background:var(--white);border:1px solid var(--line);padding:10px 12px;margin-top:10px;font-size:11.5px;color:var(--muted)}
.side-phone b{color:var(--blue)}
.widget{margin-top:14px;background:var(--white)}
.widget h4{background:var(--blue-dark);color:var(--white);font-size:12px;font-weight:700;padding:9px 10px;letter-spacing:.3px}
.widget li{list-style:none;border-bottom:1px solid var(--line);padding:8px 10px;color:var(--blue);font-size:11.5px}

/* footer */
.site-footer{background:var(--footer);height:252px;color:#d5e2ee;font-size:12.5px;padding-top:40px}
.site-footer p{margin-bottom:14px}
.site-footer a{color:var(--white);text-decoration:underline}
.footer-links{font-weight:600;color:var(--white)}
</style>
</head>
<body>

<header class="site-header">
  <div class="wrap">
    <div class="social"><span></span><span></span><span></span><span></span></div>
    <div class="topline">Call: <b>(888) 555-0142</b> – 7 Days Week</div>
    <div class="brand">
      <span class="mark"></span>
      <span class="name">Cargo Linx</span>
    </div>
    <nav class="main-nav">
      <a class="active" href="#">Home</a>
      <a href="#">Insurance &amp; Legal Info</a>
      <a href="#">Fast Freight Quote</a>
    </nav>
  </div>
</header>

<section class="hero" role="img" aria-label="Orange heavy haul truck pulling a lowboy trailer loaded with a yellow excavator on a highway under a blue sky">
  <div class="hero-caption"><h1>GET FAST &amp; FREE FREIGHT QUOTES</h1></div>
</section>

<section class="services">
  <div class="wrap">
    <p class="services-lead">Worldwide Shipping - Trucking and Ocean Service with No Limits - <a href="#">Click Here for Freight Quote</a></p>
    <div class="service-grid">
      <div class="service active">
        <div class="service-icon active">
          <svg width="54" height="40" viewBox="0 0 54 40"><rect x="2" y="8" width="30" height="20" fill="#fff"/><path d="M32 14h10l8 8v6H32z" fill="#fff"/><circle cx="12" cy="32" r="5" fill="#fff"/><circle cx="42" cy="32" r="5" fill="#fff"/></svg>
        </div>
        <h3>Heavy Haul Services</h3>
        <p>Oversized loads moved with permits, escorts and trailers built for weight.</p>
        <a class="btn-more" href="#">More</a>
      </div>
      <div class="service">
        <div class="service-icon">
          <svg width="54" height="40" viewBox="0 0 54 40"><rect x="18" y="6" width="14" height="10" fill="#fff"/><path d="M4 18h46l-7 14H11z" fill="#fff"/><path d="M2 36q6-4 12 0t12 0t12 0t12 0" stroke="#fff" stroke-width="2" fill="none"/></svg>
        </div>
        <h3>Ocean Services</h3>
        <p>Container and breakbulk cargo shipped to ports around the world on time.</p>
        <a class="btn-more" href="#">More</a>
      </div>
      <div class="service">
        <div class="service-icon">
          <svg width="54" height="40" viewBox="0 0 54 40"><rect x="10" y="4" width="34" height="24" rx="4" fill="#fff"/><circle cx="18" cy="33" r="4" fill="#fff"/><circle cx="36" cy="33" r="4" fill="#fff"/><rect x="14" y="9" width="26" height="8" fill="#1d3347"/></svg>
        </div>
        <h3>Piggy Back Service</h3>
        <p>Trailers loaded on rail cars for long haul savings across the country.</p>
        <a class="btn-more" href="#">More</a>
      </div>
      <div class="service">
        <div class="service-icon">
          <svg width="44" height="44" viewBox="0 0 44 44" stroke="#fff" stroke-width="3" stroke-linecap="round"><path d="M22 4v36M6 13l32 18M6 31l32-18"/></svg>
        </div>
        <h3>Dry &amp; Refrigerated</h3>
        <p>Dry vans and reefer units that keep goods safe and fresh in transit.</p>
        <a class="btn-more" href="#">More</a>
      </div>
    </div>
  </div>
</section>

<section class="content-band">
  <div class="wrap content-grid">
    <main class="main-col">
      <h2>GET FAST &amp; FREE FREIGHT QUOTES NOW AND SAVE!!</h2>
      <div class="bar-title">WORLDWIDE SHIPPING - OCEAN AND TRUCKING WITH NO LIMITS</div>
      <p class="text">Welcome to Cargo Linx and Broadline Freight Inc. We are a one stop solution for logistics and shipping worldwide with trucking and ocean freight services. In using our freight services we will negotiate a competitive rate with carriers across our network who are certified and contracted by us. We have set up general rules available daily, service all freight types, and have no limits worldwide.</p>
      <p class="text">Whether you need a freight quote for a full truck, LTL partial load, or oversized machinery or equipment, trucking and/or ocean shipment, we will take care of it all. Your freight or equipment to be shipped will be covered in full by our insurance with no limitations to match its value. We manage the calls, the paperwork, and the handoffs, and you get your freight moved with no hassle at a competitive shipping price!</p>
      <p class="callout">Get your freight quote online now or call 888-555-0142 now and let some of the top carriers in the country quote your business</p>
      <div class="bar-title">WORLDWIDE SHIPPING - OCEAN AND TRUCKING VIDEO</div>
      <div class="video" role="img" aria-label="Video still of a large container ship loaded with stacked containers at sea">
        <div class="play"><svg width="26" height="28" viewBox="0 0 26 28"><path d="M2 2l22 12L2 26z" fill="#fff"/></svg></div>
      </div>
      <div class="testimonial">
        <div class="avatar" role="img" aria-label="Portrait of a satisfied customer"></div>
        <div class="quote">
          <span class="mark">“</span>
          <p>Our crew needed a loader moved across three states in under a week. The team found a carrier, sorted the permits and kept us posted at every stop. The price was fair and the machine arrived without a scratch. We have used them for every shipment since then and will keep doing so.</p>
          <cite>(...Rob Hartley)</cite>
        </div>
      </div>
    </main>

    <aside class="side-col">
      <a class="quote-btn" href="#">GET A FREIGHT QUOTE<small>It's fast, easy and free</small></a>
      <div class="side-phone">Call <b>888-555-0142</b> for quotes 7 days a week</div>
      <div class="widget">
        <h4>WORLDWIDE FREIGHT SERVICES</h4>
        <ul>
          <li>Worldwide Shipping Home</li>
          <li>Trucking Shipping Services</li>
          <li>Ocean Shipping Services</li>
          <li>Insurance &amp; Legal Details</li>
          <li>Get a Freight Quote Now!</li>
          <li>Return to Home Page</li>
        </ul>
      </div>
      <div class="widget">
        <h4>FREIGHT – TRUCKING SERVICE</h4>
        <ul>
          <li>Heavy Equipment Hauling</li>
          <li>LTL Freight Transport</li>
          <li>Flatbed Transport</li>
          <li>Step Deck Transport</li>
          <li>Dry Van Transport</li>
          <li>Refrigerated Transport</li>
          <li>Power Only Transport</li>
          <li>Piggy Back Transport</li>
        </ul>
      </div>
      <div class="widget">
        <h4>OCEAN SHIPPING SERVICES</h4>
        <ul>
          <li>Heavy Equipment Hauling</li>
          <li>LTL Freight Transport</li>
          <li>Flatbed Transport</li>
          <li>Step Deck Transport</li>
          <li>Dry Van Transport</li>
          <li>Refrigerated Transport</li>
          <li>Power Only &amp; Passenger Transport</li>
        </ul>
      </div>
      <div class="widget">
        <h4>POPULAR PAGES</h4>
        <ul>
          <li>Equipment Transport</li>
          <li>Equipment Hauling</li>
          <li>Shipping Service Areas</li>
        </ul>
      </div>
    </aside>
  </div>
</section>

<footer class="site-footer">
  <div class="wrap">
    <p>Full Loads, LTL, Oversized Machinery &amp; Equipment. We do it all. All freight covered in full value by our insurance!</p>
    <p>All freight covered by a minimum of $1,000,000 in Liability and $250,000+ in Cargo Insurance with no limits Worldwide by Harbor Truck and Ocean Carrier Services!</p>
    <p>© 2014 Copyright and Owned by <a href="#">Broadline Freight Inc.</a> and <a href="#">www.cargolinx.com</a> – Equipment Transport Specialist</p>
    <p class="footer-links">Privacy Policy | Terms &amp; Conditions | Sitemap</p>
  </div>
</footer>

</body>
</html>
```